Dengue Progress Report for GHX African Region

This progress report details the GHX-led response to the dengue outbreak in Africa. It is intended for health professionals, global health leaders, and decision-makers. While the PDF BRAVO Progress report serves as an example, the focus should be on the provided Word document. Some pictures are included, but you may suggest other relevant dengue intervention images, preferably sourced from GHX.

Industry/Entity Type

Public Health

Requirements
Should not have
• As stated in the project description, the bravo document was only to illustrate GHX's preferred design style, and nothing from that report should be used.

```html
<!DOCTYPE html>
<html lang="en">
<head>
<meta charset="utf-8">
<title>Dengue Progress Report – GHX African Region</title>
<link href="https://fonts.googleapis.com/css2?family=Roboto:wght@400;500;700;900&display=swap" rel="stylesheet">
<style>
:root{
  --canvas:#ececec;
  --paper:#ffffff;
  --navy:#1b3a8c;
  --brand:#0a8fd0;
  --ink:#3a3a3a;
  --muted:#8a8a8a;
  --orange:#f28c28;
  --teal:#1aa59a;
  --purple:#6a4fb3;
  --pink:#e0457b;
}
*{box-sizing:border-box;margin:0;padding:0}
html,body{width:1200px;height:2400px;overflow:hidden}
body{background:var(--canvas);font-family:"Roboto",Arial,sans-serif;color:var(--ink);position:relative}
.page{position:absolute;width:380px;height:537px;background:var(--paper);box-shadow:0 2px 6px rgba(0,0,0,.18);overflow:hidden}
.col-left{left:220px}.col-right{left:620px}
.row-1{top:80px}.row-2{top:680px}.row-3{top:1270px}.row-4{top:1840px}

/* cover */
.cover .brand{position:absolute;top:18px;right:22px;display:flex;align-items:center;gap:6px;color:var(--brand);font-weight:700;font-size:12px}
.cover .brand .dot{width:14px;height:14px;border-radius:50%;background:var(--brand)}
.cover .brand small{display:block;font-weight:700;font-size:7px}
.cover .kicker{position:absolute;top:66px;left:120px;font-size:8px;font-weight:700;color:var(--brand);letter-spacing:.5px}
.cover .title{position:absolute;top:80px;left:120px;right:24px;font-size:12.5px;line-height:1.2;font-weight:700;color:var(--navy)}
.cover .date{position:absolute;top:168px;left:120px;font-size:7px;color:var(--muted)}
.cover .photo{position:absolute;top:190px;left:0;right:0;bottom:40px;background:linear-gradient(180deg,#dfe5e8 0%,#b9c4c3 45%,#6f7f62 80%,#4d5a3e 100%)}
.cover .base{position:absolute;left:0;right:0;bottom:0;height:40px;background:linear-gradient(180deg,#f4f6f8,#dfe8f0)}
.cover .base::before{content:"";position:absolute;left:0;right:0;top:0;height:3px;background:var(--brand)}

.back-blue{background:var(--navy)}

/* inner pages */
.inner{padding:26px 26px 30px 36px}
.inner::before{content:"";position:absolute;left:14px;top:22px;bottom:22px;width:2px;background:var(--brand)}
.inner p{font-size:5.6px;line-height:1.5;margin-bottom:5px;text-align:justify}
.inner h2{font-size:7.5px;color:var(--brand);font-weight:700;margin:6px 0 4px}
.inner .doc-head{font-size:6px;font-weight:700;color:var(--navy);line-height:1.35;margin:6px 0 10px 40px;max-width:220px}
.inner .doc-head span{display:block;color:var(--brand);font-size:5.5px}
.footer{position:absolute;left:36px;right:26px;bottom:12px;display:flex;justify-content:space-between;font-size:4.8px;color:var(--muted)}
.photo-block{width:100%;height:200px;margin-bottom:10px;background:linear-gradient(180deg,#7a8a7c 0%,#9aa59a 40%,#5e6d83 75%,#48566b 100%)}
.map-block{width:100%;height:110px;margin:6px 0 8px;background:linear-gradient(135deg,#d9ecf7,#a7cfe8 60%,#5aa6d6)}
.bullets{list-style:none;font-size:5.6px;line-height:1.6;margin-bottom:10px}
.bullets li::before{content:"•";color:var(--brand);margin-right:4px}
.tiles{display:grid;grid-template-columns:repeat(4,1fr);gap:5px;margin:8px 0}
.tile{height:56px;border-radius:3px;color:#fff;font-size:5.6px;padding:6px;display:flex;flex-direction:column;justify-content:flex-end}
.tile b{font-size:11px;font-weight:900}
.t1{background:var(--orange)}.t2{background:var(--teal)}.t3{background:var(--purple)}.t4{background:var(--pink)}
.charts{display:flex;gap:10px;margin:8px 0 10px}
.chart{flex:1}
.chart h3{font-size:5.6px;font-weight:700;color:var(--navy);margin-bottom:3px}
</style>
</head>
<body>

<section class="page cover col-right row-1">
  <div class="brand"><span class="dot"></span><div>GHX<small>African Region</small></div></div>
  <div class="kicker">PROGRESS REPORT</div>
  <h1 class="title">Managing the Unprecedented Dengue Bravo in the GHX African Region – Insights, Achievements, Challenges, and Future Directions</h1>
  <div class="date">2024</div>
  <div class="photo" role="img" aria-label="Health worker in orange protective suit fogging vegetation for mosquito control"></div>
  <div class="base"></div>
</section>

<section class="page back-blue col-left row-2"></section>

<section class="page inner col-right row-2">
  <div class="doc-head"><span>Progress Report</span>Managing the Unprecedented Dengue Bravo in the GHX African Region – Insights, Achievements, Challenges, and Future Directions</div>
  <h2>1. Executive summary</h2>
  <p>The dengue response across the region expanded rapidly this year as case counts rose in several member states. Teams strengthened surveillance, trained clinicians, and coordinated vector control with communities. This section summarises progress, gaps and the priorities agreed with national partners for the coming months.</p>
  <p>Laboratory networks confirmed serotypes in new districts, while mobile teams reached remote households with larviciding, fogging and risk communication. Supply chains for test kits and fluids improved, yet funding and staffing shortfalls still limit coverage in the most affected areas.</p>
  <p>The dengue response across the region expanded rapidly this year as case counts rose in several member states. Teams strengthened surveillance, trained clinicians, and coordinated vector control with communities. This section summarises progress, gaps and the priorities agreed with national partners for the coming months.</p>
  <p>Laboratory networks confirmed serotypes in new districts, while mobile teams reached remote households with larviciding, fogging and risk communication. Supply chains for test kits and fluids improved, yet funding and staffing shortfalls still limit coverage in the most affected areas.</p>
  <div class="footer"><span>Dengue Progress Report | GHX African Region</span><span>1</span></div>
</section>

<section class="page inner col-left row-3">
  <p>The dengue response across the region expanded rapidly this year as case counts rose in several member states. Teams strengthened surveillance, trained clinicians, and coordinated vector control with communities. This section summarises progress, gaps and the priorities agreed with national partners for the coming months.</p>
  <p>Laboratory networks confirmed serotypes in new districts, while mobile teams reached remote households with larviciding, fogging and risk communication. Supply chains for test kits and fluids improved, yet funding and staffing shortfalls still limit coverage in the most affected areas.</p>
  <h2>2. Introduction</h2>
  <p>The dengue response across the region expanded rapidly this year as case counts rose in several member states. Teams strengthened surveillance, trained clinicians, and coordinated vector control with communities. This section summarises progress, gaps and the priorities agreed with national partners for the coming months.</p>
  <p>Laboratory networks confirmed serotypes in new districts, while mobile teams reached remote households with larviciding, fogging and risk communication. Supply chains for test kits and fluids improved, yet funding and staffing shortfalls still limit coverage in the most affected areas.</p>
  <p>The dengue response across the region expanded rapidly this year as case counts rose in several member states. Teams strengthened surveillance, trained clinicians, and coordinated vector control with communities. This section summarises progress, gaps and the priorities agreed with national partners for the coming months.</p>
  <div class="footer"><span>Dengue Progress Report | GHX African Region</span><span>2</span></div>
</section>

<section class="page inner col-right row-3">
  <div class="photo-block" role="img" aria-label="Group of health workers and community members gathered outdoors during a dengue response briefing"></div>
  <h2>Coordination and leadership</h2>
  <p>The dengue response across the region expanded rapidly this year as case counts rose in several member states. Teams strengthened surveillance, trained clinicians, and coordinated vector control with communities. This section summarises progress, gaps and the priorities agreed with national partners for the coming months.</p>
  <p>Laboratory networks confirmed serotypes in new districts, while mobile teams reached remote households with larviciding, fogging and risk communication. Supply chains for test kits and fluids improved, yet funding and staffing shortfalls still limit coverage in the most affected areas.</p>
  <h2>Surveillance and data</h2>
  <p>The dengue response across the region expanded rapidly this year as case counts rose in several member states. Teams strengthened surveillance, trained clinicians, and coordinated vector control with communities. This section summarises progress, gaps and the priorities agreed with national partners for the coming months.</p>
  <div class="footer"><span>Dengue Progress Report | GHX African Region</span><span>3</span></div>
</section>

<section class="page inner col-left row-4">
  <p>Laboratory networks confirmed serotypes in new districts, while mobile teams reached remote households with larviciding, fogging and risk communication. Supply chains for test kits and fluids improved, yet funding and staffing shortfalls still limit coverage in the most affected areas.</p>
  <p>The dengue response across the region expanded rapidly this year as case counts rose in several member states. Teams strengthened surveillance, trained clinicians, and coordinated vector control with communities. This section summarises progress, gaps and the priorities agreed with national partners for the coming months.</p>
  <div class="map-block" role="img" aria-label="World map highlighting countries reporting dengue cases in blue tones"></div>
  <h2>Overview of dengue situation in the region</h2>
  <p>Laboratory networks confirmed serotypes in new districts, while mobile teams reached remote households with larviciding, fogging and risk communication. Supply chains for test kits and fluids improved, yet funding and staffing shortfalls still limit coverage in the most affected areas.</p>
  <p>The dengue response across the region expanded rapidly this year as case counts rose in several member states. Teams strengthened surveillance, trained clinicians, and coordinated vector control with communities. This section summarises progress, gaps and the priorities agreed with national partners for the coming months.</p>
  <div class="footer"><span>Dengue Progress Report | GHX African Region</span><span>4</span></div>
</section>

<section class="page inner col-right row-4">
  <ul class="bullets">
    <li>Case management: clinicians trained in triage and fluid therapy.</li>
    <li>Vector control: larviciding scaled across priority districts.</li>
    <li>Surveillance: weekly reporting from sentinel sites.</li>
    <li>Community: volunteers led clean-up campaigns in homes.</li>
  </ul>
  <div class="tiles">
    <div class="tile t1"><b>12</b>countries reporting</div>
    <div class="tile t2"><b>3,400</b>staff trained</div>
    <div class="tile t3"><b>85%</b>sites reporting</div>
    <div class="tile t4"><b>1.2M</b>people reached</div>
  </div>
  <div class="charts">
    <div class="chart">
      <h3>Weekly cases</h3>
      <svg width="150" height="80" viewBox="0 0 150 80">
        <line x1="4" y1="76" x2="148" y2="76" stroke="#bbb" stroke-width=".6"/>
        <g fill="#0a8fd0">
          <rect x="8" y="60" width="8" height="16"/><rect x="20" y="52" width="8" height="24"/>
          <rect x="32" y="40" width="8" height="36"/><rect x="44" y="28" width="8" height="48"/>
          <rect x="56" y="14" width="8" height="62"/><rect x="68" y="8" width="8" height="68"/>
          <rect x="80" y="18" width="8" height="58"/><rect x="92" y="30" width="8" height="46"/>
          <rect x="104" y="42" width="8" height="34"/><rect x="116" y="50" width="8" height="26"/>
          <rect x="128" y="58" width="8" height="18"/>
        </g>
      </svg>
    </div>
    <div class="chart">
      <h3>Tests by country</h3>
      <svg width="150" height="80" viewBox="0 0 150 80">
        <line x1="4" y1="76" x2="148" y2="76" stroke="#bbb" stroke-width=".6"/>
        <g fill="#1b3a8c">
          <rect x="10" y="20" width="12" height="56"/><rect x="30" y="34" width="12" height="42"/>
          <rect x="50" y="44" width="12" height="32"/><rect x="70" y="52" width="12" height="24"/>
          <rect x="90" y="58" width="12" height="18"/><rect x="110" y="64" width="12" height="12"/>
        </g>
        <g fill="#f28c28">
          <rect x="22" y="40" width="5" height="36"/><rect x="42" y="50" width="5" height="26"/>
          <rect x="62" y="58" width="5" height="18"/><rect x="82" y="62" width="5" height="14"/>
        </g>
      </svg>
    </div>
  </div>
  <ul class="bullets">
    <li>Sustain funding for vector control and testing.</li>
    <li>Strengthen cross-border data sharing and alerts.</li>
  </ul>
  <div class="footer"><span>Dengue Progress Report | GHX African Region</span><span>5</span></div>
</section>

</body>
</html>
```